New business card for our new logo

I have a brand new, existing logo. Now I need it on a new business card. The new card should include the following:

English language training
Translations
Interpreting Services (remote and in-person)

Target Market(s)

We are targeting international companies with foreign investment in the United States as well as domestic companies, medical offices, law offices, and non-profits that have non-native English speakers as their clients.

Contact Information for Business Card

Delia Brancombe, President
418 Garrow St.
Indianapolis, IN 46203
(317) 548-3162
info@tallpinewordworks.com
www.tallpinewordworks.com

Font styles to use
Sans Serif

Colors
0392cd
3176b5
abd036
9bcb3b
f04a50
f78f20

Requirements
Must have
• It must include our logo and business card details
Nice to have
• I would like to see a layout that is uncluttered and conveys trust and dependability, as well as the feelings of being friendly and approachable.

It would be nice to have icons for English language training, translating, and interpreting.
Should not have
• No pink, yellow, or purple

```html
<!DOCTYPE html>
<html lang="en">
<head>
<meta charset="utf-8">
<title>Tallpine Wordworks – Business Card</title>
<link href="https://fonts.googleapis.com/css2?family=Montserrat:wght@500;600;700&family=Poppins:wght@400;500&display=swap" rel="stylesheet">
<style>
  :root {
    --brand-blue: #3a6ab4;
    --accent-red: #f04a50;
    --paper: #ffffff;
    --backdrop: #2a2a2c;
  }
  * { margin: 0; padding: 0; box-sizing: border-box; }
  html, body { width: 1200px; height: 900px; overflow: hidden; background: var(--backdrop); }
  .canvas { position: relative; width: 1200px; height: 900px; }

  .card {
    position: absolute;
    left: 250px;
    width: 700px;
    height: 400px;
    border-radius: 26px;
    overflow: hidden;
    background: var(--paper);
  }
  .card--services { top: 40px; }
  .card--contact { top: 460px; }

  /* Services side */
  .services-curve { position: absolute; inset: 0; }
  .brand-lockup {
    position: absolute;
    left: 150px;
    top: 64px;
    display: flex;
    align-items: center;
    gap: 16px;
  }
  .brand-dot {
    width: 84px; height: 84px; border-radius: 50%;
    background: var(--brand-blue);
  }
  .brand-name {
    font-family: "Montserrat", sans-serif;
    font-weight: 700;
    font-size: 28px;
    line-height: 1.02;
    color: var(--brand-blue);
    white-space: nowrap;
  }
  .service-list {
    position: absolute;
    left: 0; right: 0; bottom: 34px;
    display: flex;
    justify-content: space-around;
    padding: 0 30px;
    list-style: none;
  }
  .service {
    display: flex; flex-direction: column; align-items: center; gap: 12px;
    width: 200px;
  }
  .service-icon {
    width: 62px; height: 62px; border-radius: 50%;
    background: var(--paper);
  }
  .service-label {
    font-family: "Poppins", sans-serif;
    font-size: 16px;
    color: var(--paper);
    text-align: center;
    white-space: nowrap;
  }

  /* Contact side */
  .contact-text { position: absolute; left: 44px; top: 38px; }
  .company-name {
    font-family: "Montserrat", sans-serif;
    font-weight: 700;
    font-size: 40px;
    line-height: 1.0;
    color: var(--brand-blue);
  }
  .person-name {
    margin-top: 34px;
    font-family: "Montserrat", sans-serif;
    font-weight: 700;
    font-size: 26px;
    color: var(--brand-blue);
  }
  .person-title {
    font-family: "Poppins", sans-serif;
    font-size: 18px;
    color: var(--accent-red);
    margin-bottom: 12px;
  }
  .contact-list { list-style: none; }
  .contact-item {
    display: flex; align-items: center; gap: 10px;
    font-family: "Poppins", sans-serif;
    font-size: 15.5px;
    color: var(--brand-blue);
    line-height: 1;
    margin-bottom: 9px;
  }
  .contact-icon { width: 24px; height: 24px; flex: none; }
  .logo-disc {
    position: absolute;
    right: 40px; top: 40px;
    width: 300px; height: 300px;
    border-radius: 50%;
    background: var(--brand-blue);
  }
</style>
</head>
<body>
<main class="canvas">

  <section class="card card--services" aria-label="Card back: services">
    <svg class="services-curve" viewBox="0 0 700 400" preserveAspectRatio="none" aria-hidden="true">
      <rect width="700" height="400" fill="var(--brand-blue)"/>
      <path d="M0 0 H600 C560 190 340 275 0 220 Z" fill="var(--paper)"/>
    </svg>

    <div class="brand-lockup">
      <div class="brand-dot" aria-hidden="true"></div>
      <div class="brand-name">Tallpine<br>Wordworks</div>
    </div>

    <ul class="service-list">
      <li class="service">
        <div class="service-icon" role="img" aria-label="English language training icon"></div>
        <span class="service-label">English language training</span>
      </li>
      <li class="service">
        <div class="service-icon" role="img" aria-label="Translations icon"></div>
        <span class="service-label">Translations</span>
      </li>
      <li class="service">
        <div class="service-icon" role="img" aria-label="Interpreting services icon"></div>
        <span class="service-label">Interpreting Services</span>
      </li>
    </ul>
  </section>

  <section class="card card--contact" aria-label="Card front: contact details">
    <div class="logo-disc" aria-hidden="true"></div>

    <div class="contact-text">
      <h1 class="company-name">Tallpine<br>Wordworks</h1>
      <p class="person-name">Delia Brancombe</p>
      <p class="person-title">President</p>
      <ul class="contact-list">
        <li class="contact-item">
          <svg class="contact-icon" viewBox="0 0 24 24" aria-hidden="true">
            <circle cx="12" cy="12" r="12" fill="var(--accent-red)"/>
            <path d="M8.2 6.5l2 2.2-1.1 1.4c.8 1.7 2 2.9 3.7 3.7l1.4-1.1 2.2 2-1.1 1.8c-4.1-.3-7.9-4.1-8.2-8.2z" fill="#fff"/>
          </svg>
          (317) 548-3162
        </li>
        <li class="contact-item">
          <svg class="contact-icon" viewBox="0 0 24 24" aria-hidden="true">
            <circle cx="12" cy="12" r="12" fill="var(--accent-red)"/>
            <rect x="6" y="8" width="12" height="8.5" rx="1" fill="none" stroke="#fff" stroke-width="1.5"/>
            <path d="M6.5 8.5l5.5 4.3 5.5-4.3" fill="none" stroke="#fff" stroke-width="1.5"/>
          </svg>
          info@tallpinewordworks.com
        </li>
        <li class="contact-item">
          <svg class="contact-icon" viewBox="0 0 24 24" aria-hidden="true">
            <circle cx="12" cy="12" r="12" fill="var(--accent-red)"/>
            <g fill="none" stroke="#fff" stroke-width="1.3">
              <circle cx="12" cy="12" r="6"/>
              <ellipse cx="12" cy="12" rx="2.6" ry="6"/>
              <path d="M6 12h12M7 9h10M7 15h10"/>
            </g>
          </svg>
          www.tallpinewordworks.com
        </li>
        <li class="contact-item">
          <svg class="contact-icon" viewBox="0 0 24 24" aria-hidden="true">
            <circle cx="12" cy="12" r="12" fill="var(--accent-red)"/>
            <path d="M12 5.5a4.5 4.5 0 0 1 4.5 4.5c0 3.3-4.5 8-4.5 8s-4.5-4.7-4.5-8A4.5 4.5 0 0 1 12 5.5z" fill="#fff"/>
            <circle cx="12" cy="10" r="1.7" fill="var(--accent-red)"/>
          </svg>
          418 Garrow St, Indianapolis, IN 46203
        </li>
      </ul>
    </div>
  </section>

</main>
</body>
</html>
```